I need a fresh looking, exciting and loaded design for Full service Restaurant

We need a web design for our restaurant, which offers full service Pakistani and Indian food in PA, USA. Design should be elegant, simplified so customers can navigate easily and order food online for catering as well as delivery. We need loads of pictures and room to grow. I already have a web address via vexlorin.com. It should include SSL and e-commerce for ordering food.
Be original and be creative and make it a fun site :)

Industry/Entity Type

Restaurant

```html
<!DOCTYPE html>
<html lang="en">
<head>
<meta charset="utf-8">
<title>Saffron Hearth – Home</title>
<link href="https://fonts.googleapis.com/css2?family=Raleway:wght@400;500;600;700&family=Great+Vibes&display=swap" rel="stylesheet">
<style>
:root{
  --red:#d7091b;
  --red-deep:#c10616;
  --ink:#555555;
  --ink-soft:#8a8a8a;
  --paper:#f7f7f7;
  --white:#ffffff;
  --footer:#111111;
  --footer-text:#c9c9c9;
}
*{margin:0;padding:0;box-sizing:border-box}
html,body{width:1200px;height:739px;overflow:hidden;background:var(--paper)}
body{font-family:"Raleway",Arial,sans-serif;position:relative}
.page{position:relative;width:1200px;height:739px;overflow:hidden;background:var(--paper)}

.brand{position:absolute;left:86px;top:40px;display:flex;align-items:center;gap:8px;color:var(--red);font-weight:700;font-size:24px;letter-spacing:.2px}
.brand-dot{width:14px;height:14px;border-radius:50%;background:var(--red)}

.main-nav{position:absolute;top:50px;left:629px;display:flex;gap:0;font-size:13.5px;font-weight:500;color:var(--ink)}
.main-nav a{color:inherit;text-decoration:none;position:absolute;white-space:nowrap}
.main-nav .active{color:var(--red);font-weight:600}
.btn-outline{position:absolute;border:1px solid var(--red);color:var(--red);border-radius:18px;font-weight:600;font-size:13.5px;display:flex;align-items:center;justify-content:center;text-decoration:none}
.header-order{left:920px;top:42px;width:134px;height:33px}
.search-icon{position:absolute;left:1097px;top:51px}

.tagline{position:absolute;left:848px;top:130px;width:300px;height:160px;color:var(--ink-soft)}
.tagline .lead{position:absolute;left:2px;top:32px;font-size:19px;font-weight:400}
.tagline .script{position:absolute;left:52px;top:-8px;font-family:"Great Vibes",cursive;font-size:96px;color:var(--red);line-height:1}
.tagline .trail{position:absolute;left:92px;top:76px;font-size:29px;font-weight:300;letter-spacing:.5px}

.slide-dots{position:absolute;left:1105px;top:306px;display:flex;flex-direction:column;gap:8px}
.slide-dots span{width:9px;height:9px;border-radius:50%;border:1px solid #9a9a9a}
.slide-dots .current{background:var(--red);border-color:var(--red)}

.hero-band{position:absolute;left:0;top:0}
.dish-photo{position:absolute;left:292px;top:252px;width:612px;height:264px;border-radius:50%;
  background:radial-gradient(ellipse at 55% 45%,#c9b08a 0%,#a88c64 35%,#e9e6e1 62%,#ffffff 80%);
  box-shadow:0 14px 24px rgba(0,0,0,.25)}

.hero-copy{position:absolute;left:200px;top:538px;width:800px;text-align:center;color:var(--white);font-size:13.5px;font-weight:600;line-height:16px}
.btn-solid{position:absolute;left:496px;top:594px;width:208px;height:44px;background:var(--white);color:var(--red-deep);border-radius:22px;display:flex;align-items:center;justify-content:center;font-weight:700;font-size:13.5px;text-decoration:none;box-shadow:0 4px 10px rgba(0,0,0,.2)}
.arrow{position:absolute;top:606px}
.arrow-prev{left:87px}
.arrow-next{left:1091px}

.site-footer{position:absolute;left:0;top:671px;width:1200px;height:68px;background:var(--footer);color:var(--footer-text);font-size:13px}
.copyright{position:absolute;left:162px;top:26px}
.footer-nav a{position:absolute;top:26px;color:var(--footer-text);text-decoration:none;white-space:nowrap}
.footer-nav .active{color:var(--red);font-weight:600}
.footer-order{left:980px;top:18px;width:134px;height:33px}
</style>
</head>
<body>
<div class="page">

  <svg class="hero-band" width="1200" height="739" viewBox="0 0 1200 739" aria-hidden="true">
    <path d="M0 536 C 160 420, 380 378, 600 378 C 830 378, 1060 420, 1200 474 L1200 671 L0 671 Z" fill="var(--red)"/>
  </svg>

  <header>
    <div class="brand"><span class="brand-dot"></span>Saffron Hearth</div>
    <nav class="main-nav">
      <a class="active" style="left:0;top:0">HOME</a>
      <a style="left:75px;top:0">ABOUT US</a>
      <a style="left:177px;top:0">RECIPES</a>
    </nav>
    <a class="btn-outline header-order">ONLINE ORDER</a>
    <svg class="search-icon" width="18" height="18" viewBox="0 0 18 18" aria-label="Search">
      <circle cx="7.5" cy="7.5" r="6" fill="none" stroke="var(--red)" stroke-width="1.5"/>
      <line x1="12" y1="12" x2="17" y2="17" stroke="var(--red)" stroke-width="1.5"/>
    </svg>
  </header>

  <div class="tagline">
    <span class="lead">ADD A</span>
    <span class="script">Spice</span>
    <span class="trail">TO YOUR LIFE...</span>
  </div>

  <div class="slide-dots"><span></span><span class="current"></span><span></span></div>

  <div class="dish-photo" role="img" aria-label="Grilled chicken kebabs on a white plate with salad garnish"></div>

  <p class="hero-copy">Duis autem vel eum iriure dolor in hendrerit in vulputate velit esse molestie consequat, vel illum dolore eu feugiat nulla facilisis at verot luptatum zzril delenit augue duis dolore te feugait nulla facilisi.</p>

  <a class="btn-solid">PLACE ORDER</a>

  <svg class="arrow arrow-prev" width="24" height="20" viewBox="0 0 24 20" aria-label="Previous slide">
    <path d="M23 10H2M10 2L2 10l8 8" fill="none" stroke="var(--white)" stroke-width="2"/>
  </svg>
  <svg class="arrow arrow-next" width="24" height="20" viewBox="0 0 24 20" aria-label="Next slide">
    <path d="M1 10h21M14 2l8 8-8 8" fill="none" stroke="var(--white)" stroke-width="2"/>
  </svg>

  <footer class="site-footer">
    <span class="copyright">© Copyright 2015.</span>
    <nav class="footer-nav">
      <a class="active" style="left:507px">HOME</a>
      <a style="left:582px">ABOUT US</a>
      <a style="left:687px">RECIPES</a>
      <a style="left:777px">BLOG</a>
      <a style="left:857px">CONTACT US</a>
    </nav>
    <a class="btn-outline footer-order">ONLINE ORDER</a>
  </footer>

</div>
</body>
</html>
```